Wellness company needs a flyer for our new green powder drink.

We need a flyer for our new green powder drink which has 14 ingredients, am attaching images and descriptions for each ingredient. Will be a one sided flyer please on 8.5 by 11 paper. Each photo should be placed next to each product description.
Updates

The flyer size should be 8.5 by 11. The photos should be placed next to each product description. You can see the product on our website: https://www.tormiqhealth.com/products/leaf-surge/ I will also upload an image of the product label.

Target Market(s)

Health minded people

Industry/Entity Type

Health And Wellness

Requirements
Must have
• Please choose from the images upload and I'm including to product descriptions. If there is room on the flyer use the longer descriptions. You can see our colors & feel on our website www.tormiqhealth.com
Nice to have
• Must use the images with ingredient descriptions

```html
<!DOCTYPE html>
<html lang="en">
<head>
<meta charset="utf-8">
<title>Leaf Surge Ingredients – Tormiq Health</title>
<link href="https://fonts.googleapis.com/css2?family=Oswald:wght@400;500&family=Roboto:wght@400;500&display=swap" rel="stylesheet">
<style>
  :root {
    --page-bg: #e3d0b8;
    --sheet-top: #ffffff;
    --sheet-bottom: #eef3e6;
    --orange: #f0a04b;
    --green: #6aa82c;
    --title-green: #7db843;
    --text: #4a4a4a;
    --ring: #ffffff;
  }
  * { box-sizing: border-box; margin: 0; padding: 0; }
  html, body { width: 1200px; height: 900px; overflow: hidden; }
  body {
    background: var(--page-bg);
    font-family: "Roboto", Arial, sans-serif;
    color: var(--text);
    position: relative;
  }
  .flyer {
    position: absolute;
    left: 260px; top: 10px;
    width: 680px; height: 880px;
    background: linear-gradient(160deg, var(--sheet-top) 0%, var(--sheet-top) 35%, var(--sheet-bottom) 100%);
    box-shadow: 0 10px 30px rgba(90, 60, 30, .25);
    overflow: hidden;
  }
  .top-band {
    height: 30px;
    background: var(--orange);
    display: flex; justify-content: space-between; align-items: center;
    padding: 0 22px;
    font-family: "Oswald", "Arial Narrow", sans-serif;
    color: #fff; letter-spacing: 1.5px; font-size: 13px; font-weight: 500;
  }
  .top-band .site { font-size: 10px; letter-spacing: 2px; }
  .brand {
    position: absolute; left: 20px; top: 66px;
    display: flex; align-items: center; gap: 8px;
  }
  .brand-dot { width: 32px; height: 32px; border-radius: 50%; background: var(--green); flex: none; }
  .brand-name { font-size: 17px; font-weight: 500; color: var(--green); white-space: nowrap; }
  .intro {
    position: absolute; left: 190px; top: 50px; width: 170px;
    font-size: 10px; line-height: 1.4; font-weight: 500; color: #3c3c3c;
  }
  .divider {
    position: absolute; left: 0; top: 178px; width: 200px; height: 1px;
    background: #d9d9d9;
  }
  .column { position: absolute; display: flex; flex-direction: column; }
  .column.left { left: 18px; top: 192px; gap: 10px; }
  .column.right { left: 370px; top: 40px; gap: 12px; }
  .ingredient { display: flex; align-items: center; gap: 12px; height: 96px; }
  .photo {
    flex: none; width: 92px; height: 92px; border-radius: 50%;
    border: 5px solid var(--ring);
    box-shadow: 0 1px 6px rgba(0, 0, 0, .18);
  }
  .info { width: 200px; }
  .info h2 {
    font-family: "Oswald", "Arial Narrow", sans-serif;
    font-size: 11px; font-weight: 500; color: var(--title-green);
    text-transform: uppercase; letter-spacing: .4px; margin-bottom: 2px;
  }
  .info p { font-size: 8.6px; line-height: 1.35; }
  .bottom-band {
    position: absolute; left: 0; bottom: 0; width: 100%; height: 36px;
    background: var(--green); color: #fff;
    display: flex; align-items: center; justify-content: center;
    font-size: 11.5px; font-weight: 500;
  }
  .spirulina { background: radial-gradient(circle at 40% 40%, #2f5a2e, #16301a); }
  .alfalfa { background: radial-gradient(circle, #7cbf4a, #f4f4f0 75%); }
  .dandelion { background: radial-gradient(circle at 50% 40%, #f3c316 20%, #2f4a1c 70%); }
  .lemon { background: radial-gradient(circle, #f5d928 45%, #fbfbf5 75%); }
  .chlorella { background: radial-gradient(circle at 45% 55%, #2e6a26, #6b6b66); }
  .dulse { background: radial-gradient(circle, #8a3d22 35%, #f5f2ee 75%); }
  .spinach { background: radial-gradient(circle, #3f8f2a 50%, #f7f7f3 80%); }
  .barley { background: radial-gradient(circle, #8fbf5a 45%, #f5f5f0 78%); }
  .wheatgrass { background: radial-gradient(circle, #5f9f37 35%, #9ea4a2 75%); }
  .moringa { background: radial-gradient(circle, #2f9a2f 50%, #f5f8f2 80%); }
  .kelp { background: radial-gradient(circle, #2b4a1a 55%, #f4f4f0 85%); }
  .orange-peel { background: radial-gradient(circle, #f08a1c 45%, #fbf6f0 78%); }
  .beet { background: radial-gradient(circle, #5a1a3a 50%, #2f4a22 85%); }
</style>
</head>
<body>
<main class="flyer">
  <header class="top-band">
    <span class="title">LEAF SURGE INGREDIENTS</span>
    <span class="site">WWW.TORMIQHEALTH.COM</span>
  </header>

  <div class="brand">
    <span class="brand-dot"></span>
    <span class="brand-name">Tormiq Health</span>
  </div>
  <p class="intro">Leaf Surge is the latest in the Tormiq Health line of products. It's a green drink formulation that can be added to a smoothie, juice, or added to recipes. Read on to find out what is included in our Leaf Surge green drink!</p>
  <div class="divider"></div>

  <section class="column left">
    <article class="ingredient">
      <div class="photo barley" role="img" aria-label="Barley grass powder and fresh blades"></div>
      <div class="info"><h2>Organic Barley Grass</h2><p>Barley grass juice is nutrient-dense, providing you with the following: beta carotene, B vitamins, pantothenic acid, folic acid, minerals, chlorophyll, amino acids, protein, fiber, and enzymes.</p></div>
    </article>
    <article class="ingredient">
      <div class="photo wheatgrass" role="img" aria-label="Wheatgrass bundles with a bowl of green powder"></div>
      <div class="info"><h2>Organic Wheatgrass</h2><p>The leaves of young wheatgrass are rich in iron, calcium, enzymes, essential vitamins and minerals, amino acids, and chlorophyll. The phytonutrients in wheatgrass support the immune system and general wellbeing.</p></div>
    </article>
    <article class="ingredient">
      <div class="photo moringa" role="img" aria-label="Fresh moringa leaves"></div>
      <div class="info"><h2>Organic Moringa Leaf</h2><p>Moringa leaf is high in essential micronutrients, including calcium, zinc, iron, magnesium, potassium, and vitamins A and C. It is also a complete protein, contains fiber, also packed with antioxidants!</p></div>
    </article>
    <article class="ingredient">
      <div class="photo kelp" role="img" aria-label="Dark green kelp seaweed"></div>
      <div class="info"><h2>Organic Kelp</h2><p>Kelp is very high in nutrients, a source of vitamin B, calcium, potassium, iodine, iron, and magnesium. Sea kelp mitigates iodine deficiency, which is essential for thyroid function.</p></div>
    </article>
    <article class="ingredient">
      <div class="photo orange-peel" role="img" aria-label="Curled orange peel and slices"></div>
      <div class="info"><h2>Organic Orange Peel</h2><p>Oranges peel is high in flavonoids, calcium, folate, riboflavin, thiamin, niacin, and Vitamins A, C, B5, and B6. The nutritional profile means that oranges are great for anti-inflammation and overall health.</p></div>
    </article>
    <article class="ingredient">
      <div class="photo beet" role="img" aria-label="Fresh beetroots with leaves"></div>
      <div class="info"><h2>Organic Beet Root</h2><p>Beetroot is rich in nitrates, which becomes nitric oxide upon consumption. This chain reaction may help to improve blood flow and decrease blood pressure. It also contains dense amounts of antioxidants, fiber, Vitamin C, folate, and potassium.</p></div>
    </article>
  </section>

  <section class="column right">
    <article class="ingredient">
      <div class="photo spirulina" role="img" aria-label="Spirulina powder in a wooden bowl"></div>
      <div class="info"><h2>Organic Spirulina</h2><p>Spirulina contains protein, B vitamins, calcium, potassium, magnesium, zinc, and iron. Spirulina is also rich in antioxidants and healthy fatty acids.</p></div>
    </article>
    <article class="ingredient">
      <div class="photo alfalfa" role="img" aria-label="Alfalfa sprouts"></div>
      <div class="info"><h2>Organic Alfalfa Leaf</h2><p>Alfalfa is a source of Vitamins A, C, E, and K4. It is also a source of minerals, including iron, zinc, phosphorous, and calcium.</p></div>
    </article>
    <article class="ingredient">
      <div class="photo dandelion" role="img" aria-label="Yellow dandelion flowers"></div>
      <div class="info"><h2>Organic Dandelion Leaf</h2><p>Dandelion leaf is a rich source of B complex vitamins, beta-carotene, antioxidants, potassium, iron, calcium, zinc, magnesium, and phosphorus. The leaves and roots even contain fiber and protein.</p></div>
    </article>
    <article class="ingredient">
      <div class="photo lemon" role="img" aria-label="Lemon halves and peel"></div>
      <div class="info"><h2>Lemon Peel</h2><p>Lemon peel is very high in flavonoids, calcium, folate, riboflavin, thiamin, niacin, and Vitamins A, C, B5, and B6.</p></div>
    </article>
    <article class="ingredient">
      <div class="photo chlorella" role="img" aria-label="Chlorella powder with a wooden scoop"></div>
      <div class="info"><h2>Organic Chlorella</h2><p>Chlorella contains dense amounts of protein, Vitamins B and C, iron, calcium, and Omega-3s.</p></div>
    </article>
    <article class="ingredient">
      <div class="photo dulse" role="img" aria-label="Red dulse seaweed"></div>
      <div class="info"><h2>Organic Dulse Leaf</h2><p>Dulse leaf is high in B vitamins, potassium, iron, and iodine. Dulse leaf also has fiber and protein. Dulse leaf is thought to help regulate blood pressure, keep the eyes healthy, and improve thyroid function.</p></div>
    </article>
    <article class="ingredient">
      <div class="photo spinach" role="img" aria-label="Fresh spinach leaves"></div>
      <div class="info"><h2>Organic Spinach Leaf</h2><p>Spinach is very nutrient-dense, supplying several essential vitamins and minerals, especially iron. Spinach also contains zeaxanthin for eye health, nitrates for heart health, lutein for eye health, and kaempferol and quercetin (both antioxidants).</p></div>
    </article>
  </section>

  <footer class="bottom-band">Visit www.tormiqhealth.com to find out more about Leaf Surge and our full line of products!</footer>
</main>
</body>
</html>
```